Lakemont Harmony Medical Tri-Fold Flyer

a marketing 3- fold flyer for primary business awareness. this should offer all aspects of our medical practice. I have provided several pictures as well as all pertinent information needed to make a successful flyer. This needs to be eye catching and attractive. each page should feature something of its own.
my thoughts:
page 1- photo of office our mission statement and maybe our phone number and address
page 2- our LHM A-team flyer
page 3- our paragraph on our practice as well as some of our services. say something like we offer a wide scope of services including health coaching, weight loss. A "patient services coordinator" will help you pick out what services we can do for you. a pic
page 4- doctors bio and pics and logos
page 5-
page 6- our map our address and phone numbers. the sentence on making an appointment. our web page and facebook as well as our logos

Target Market(s)

we are a medical practice, so we are seeking new patients

Industry/Entity Type

Health Care

Font styles to use
Serif

Colors
34a6d7
33b8a4
abd036
fbee3e

Requirements
Must have
• I have enclosed a tri-fold info attachment as well as other pieces. Use what you feel will make our flyer attractive. Not too busy. Please try to get most info in
• All work purchased should be delivered with the PDF form for future changes by owner of medical office.
Nice to have
• All Info provided

```html
<!DOCTYPE html>
<html lang="en">
<head>
<meta charset="utf-8">
<title>Lakemont Harmony Medical – Tri-Fold Flyer</title>
<link href="https://fonts.googleapis.com/css2?family=Open+Sans:wght@400;600;700&family=Lora:wght@500;700&display=swap" rel="stylesheet">
<style>
  :root {
    --bg: #e8eaed;
    --paper: #ffffff;
    --blue: #2b82b3;
    --blue-dark: #1d5e87;
    --blue-deep: #174c6e;
    --blue-light: #34a6d7;
    --teal: #33b8a4;
    --green: #abd036;
    --ink: #3a4650;
    --ink-soft: #6b7780;
    --line: #d6dde3;
  }
  * { box-sizing: border-box; margin: 0; padding: 0; }
  html, body { width: 1200px; height: 2400px; overflow: hidden; }
  body {
    background: var(--bg);
    font-family: "Open Sans", Arial, sans-serif;
    color: var(--ink);
    position: relative;
  }
  .spread {
    position: absolute;
    left: 50px;
    width: 1100px;
    height: 850px;
    display: grid;
    grid-template-columns: repeat(3, 1fr);
    background: var(--paper);
    box-shadow: 0 6px 24px rgba(0,0,0,.12);
  }
  .spread--outside { top: 250px; }
  .spread--inside { top: 1300px; }
  .panel { position: relative; overflow: hidden; height: 850px; }
  .panel + .panel { border-left: 1px solid rgba(0,0,0,.06); }

  .photo { position: absolute; }
  .brand {
    display: flex; align-items: center; gap: 10px;
    font-family: "Open Sans", Arial, sans-serif;
    font-weight: 700; color: var(--blue-dark);
    letter-spacing: .5px;
  }
  .brand__dot { width: 22px; height: 22px; border-radius: 50%; background: var(--blue-light); flex: none; }

  /* Back flap */
  .flap .brand { position: absolute; top: 34px; left: 32px; font-size: 19px; }
  .flap__intro { position: absolute; top: 92px; left: 32px; right: 32px; font-size: 12px; line-height: 1.6; color: var(--ink-soft); }
  .flap__diagram { position: absolute; top: 175px; left: 18px; width: 330px; height: 330px; }
  .flap__photo { top: 560px; left: 0; width: 100%; height: 230px; background: linear-gradient(135deg, #8fbf6a, #d7c4a8 60%, #a8865e); }
  .flap__curve { position: absolute; top: 520px; left: 0; width: 100%; height: 80px; }
  .flap__base { position: absolute; bottom: 0; left: 0; width: 100%; height: 60px; background: var(--blue-dark); color: #fff; font-size: 12px; display: flex; align-items: center; justify-content: center; letter-spacing: .5px; }

  /* Back panel */
  .back { background: var(--blue); color: #fff; }
  .back__photo { top: 0; left: 0; width: 100%; height: 260px; background: linear-gradient(180deg, #a9c4d8, #6f7f8c 55%, #4a5660); }
  .back__body { position: absolute; top: 285px; left: 30px; right: 30px; }
  .back__title { font-family: "Lora", Georgia, serif; font-size: 20px; font-weight: 700; margin-bottom: 10px; }
  .back__text { font-size: 12px; line-height: 1.65; opacity: .95; }
  .back__map { top: 520px; left: 30px; width: calc(100% - 60px); height: 150px; background: linear-gradient(135deg, #eef1f3, #d7dde2); border: 4px solid #fff; }
  .back__cta { position: absolute; top: 690px; left: 30px; right: 30px; background: var(--blue-light); border-radius: 20px; padding: 9px 0; text-align: center; font-weight: 700; font-size: 13px; letter-spacing: .5px; }
  .contact { position: absolute; top: 740px; left: 30px; right: 30px; font-size: 12px; line-height: 1.9; }
  .contact__row { display: flex; align-items: center; gap: 8px; }
  .contact__row svg { flex: none; }

  /* Cover */
  .cover .brand { position: absolute; top: 58px; left: 40px; font-size: 22px; }
  .cover__swoosh { position: absolute; top: 110px; left: 0; width: 100%; height: 90px; }
  .cover__photo { top: 175px; left: 0; width: 100%; height: 470px; background: linear-gradient(160deg, #d9e3ea, #9aa9b4 45%, #5e6c77); }
  .cover__wave { position: absolute; top: 600px; left: 0; width: 100%; height: 90px; }
  .cover__band { position: absolute; top: 680px; bottom: 0; left: 0; width: 100%; background: var(--blue); }
  .cover__tagline { position: absolute; top: 712px; right: 36px; font-family: "Lora", Georgia, serif; font-size: 24px; color: #fff; font-weight: 500; }
  .cover__sub { position: absolute; top: 752px; right: 36px; font-size: 12px; color: rgba(255,255,255,.8); }

  /* Inside left */
  .intro__photo { top: 0; left: 0; width: 100%; height: 330px; background: linear-gradient(180deg, #7aa85a, #6c8f4a 50%, #b5533e 75%, #c96a4f); }
  .intro__curve { position: absolute; top: 280px; left: 0; width: 100%; height: 80px; }
  .intro__body { position: absolute; top: 380px; left: 32px; right: 32px; }
  .intro__title { font-family: "Lora", Georgia, serif; font-size: 22px; color: var(--blue-dark); font-weight: 700; margin-bottom: 14px; }
  .intro__text { font-size: 12px; line-height: 1.7; color: var(--ink-soft); margin-bottom: 12px; }

  /* Services */
  .services { background: var(--blue-dark); color: #fff; }
  .services__title { position: absolute; top: 48px; left: 34px; font-family: "Lora", Georgia, serif; font-size: 20px; font-weight: 700; }
  .services__list { position: absolute; top: 96px; left: 34px; right: 30px; list-style: none; font-size: 13px; }
  .services__list li { display: flex; align-items: center; gap: 10px; padding: 6px 0; border-bottom: 1px solid rgba(255,255,255,.12); }
  .services__list svg { flex: none; }
  .services__note { position: absolute; top: 500px; left: 34px; right: 30px; font-size: 12px; line-height: 1.6; opacity: .9; }
  .services__photo { top: 600px; left: 0; width: 100%; height: 250px; background: linear-gradient(135deg, #f2f4f6, #cfd8df 60%, #8aa6bb); border-top-left-radius: 60px; }

  /* Doctors */
  .doctors { background: var(--blue); color: #fff; }
  .doctor { position: absolute; left: 34px; right: 34px; text-align: center; }
  .doctor--one { top: 48px; }
  .doctor--two { top: 448px; }
  .doctor__photo { width: 130px; height: 130px; border-radius: 50%; margin: 0 auto 14px; border: 5px solid #fff; background: linear-gradient(135deg, #c9a78d, #7a6655); }
  .doctor__name { font-family: "Lora", Georgia, serif; font-size: 18px; font-weight: 700; }
  .doctor__role { font-size: 12px; opacity: .85; margin-bottom: 10px; }
  .doctor__bio { font-size: 12px; line-height: 1.6; opacity: .95; }
</style>
</head>
<body>

<section class="spread spread--outside">
  <!-- Back flap -->
  <article class="panel flap">
    <div class="brand"><span class="brand__dot"></span>Lakemont Harmony Medical</div>
    <p class="flap__intro">Caring for body, mind and lifestyle under one roof. Our team builds a plan that fits you and your family.</p>
    <svg class="flap__diagram" viewBox="0 0 330 330" aria-label="Whole-person care areas">
      <g stroke="#9fc6de" stroke-width="1.5">
        <line x1="165" y1="165" x2="165" y2="45"/><line x1="165" y1="165" x2="269" y2="105"/>
        <line x1="165" y1="165" x2="269" y2="225"/><line x1="165" y1="165" x2="165" y2="285"/>
        <line x1="165" y1="165" x2="61" y2="225"/><line x1="165" y1="165" x2="61" y2="105"/>
      </g>
      <circle cx="165" cy="165" r="52" fill="#2b82b3"/>
      <text x="165" y="160" fill="#fff" font-family="Open Sans, sans-serif" font-size="12" font-weight="700" text-anchor="middle">Whole</text>
      <text x="165" y="176" fill="#fff" font-family="Open Sans, sans-serif" font-size="12" font-weight="700" text-anchor="middle">Person Care</text>
      <g fill="#fff" stroke="#34a6d7" stroke-width="2">
        <circle cx="165" cy="45" r="34"/><circle cx="269" cy="105" r="34"/><circle cx="269" cy="225" r="34"/>
        <circle cx="165" cy="285" r="34"/><circle cx="61" cy="225" r="34"/><circle cx="61" cy="105" r="34"/>
      </g>
      <g fill="#1d5e87" font-family="Open Sans, sans-serif" font-size="10" font-weight="600" text-anchor="middle">
        <text x="165" y="49">Nutrition</text><text x="269" y="109">Fitness</text><text x="269" y="229">Coaching</text>
        <text x="165" y="289">Primary</text><text x="61" y="229">Weight</text><text x="61" y="109">Wellness</text>
      </g>
    </svg>
    <svg class="flap__curve" viewBox="0 0 367 80" preserveAspectRatio="none"><path d="M0 40 Q180 0 367 30 L367 80 L0 80 Z" fill="#34a6d7"/></svg>
    <div class="photo flap__photo" role="img" aria-label="Photo of a smiling mother and daughter"></div>
    <div class="flap__base">Your health, our shared goal</div>
  </article>

  <!-- Back panel -->
  <article class="panel back">
    <div class="photo back__photo" role="img" aria-label="Photo of the medical office building"></div>
    <div class="back__body">
      <h2 class="back__title">Our Mission</h2>
      <p class="back__text">We partner with every patient to restore balance and lasting health, blending proven medicine with natural, personal care delivered by a team that listens.</p>
    </div>
    <div class="photo back__map" role="img" aria-label="Map showing the office location"></div>
    <div class="back__cta">Make an Appointment Today</div>
    <div class="contact">
      <div class="contact__row">
        <svg width="14" height="14" viewBox="0 0 24 24"><path fill="#fff" d="M6.6 10.8a15.1 15.1 0 0 0 6.6 6.6l2.2-2.2a1 1 0 0 1 1-.25 11.4 11.4 0 0 0 3.6.57 1 1 0 0 1 1 1V20a1 1 0 0 1-1 1A17 17 0 0 1 3 4a1 1 0 0 1 1-1h3.5a1 1 0 0 1 1 1c0 1.25.2 2.45.57 3.57a1 1 0 0 1-.25 1z"/></svg>
        (555) 014-2290
      </div>
      <div class="contact__row">
        <svg width="14" height="14" viewBox="0 0 24 24"><path fill="#fff" d="M12 2a7 7 0 0 0-7 7c0 5.2 7 13 7 13s7-7.8 7-13a7 7 0 0 0-7-7zm0 9.5A2.5 2.5 0 1 1 12 6.5a2.5 2.5 0 0 1 0 5z"/></svg>
        1420 Lakemont Avenue, Suite 200
      </div>
      <div class="contact__row">www.lakemontharmony.example</div>
    </div>
  </article>

  <!-- Cover -->
  <article class="panel cover">
    <div class="brand"><span class="brand__dot"></span>Lakemont Harmony Medical</div>
    <svg class="cover__swoosh" viewBox="0 0 367 90" preserveAspectRatio="none"><path d="M0 60 Q200 10 367 30 L367 90 L0 90 Z" fill="#34a6d7"/><path d="M0 75 Q200 30 367 50 L367 90 L0 90 Z" fill="#1d5e87"/></svg>
    <div class="photo cover__photo" role="img" aria-label="Photo of a couple running on treadmills"></div>
    <svg class="cover__wave" viewBox="0 0 367 90" preserveAspectRatio="none"><path d="M0 60 Q180 0 367 40 L367 90 L0 90 Z" fill="#34a6d7"/><path d="M0 85 Q180 30 367 70 L367 90 L0 90 Z" fill="#2b82b3"/></svg>
    <div class="cover__band"></div>
    <p class="cover__tagline">We Create Healthy People</p>
    <p class="cover__sub">Integrative care for the whole family</p>
  </article>
</section>

<section class="spread spread--inside">
  <!-- Inside left -->
  <article class="panel intro">
    <div class="photo intro__photo" role="img" aria-label="Photo of a man running on an outdoor track"></div>
    <svg class="intro__curve" viewBox="0 0 367 80" preserveAspectRatio="none"><path d="M0 50 Q180 0 367 40 L367 80 L0 80 Z" fill="#34a6d7"/><path d="M0 65 Q180 20 367 55 L367 80 L0 80 Z" fill="#fff"/></svg>
    <div class="intro__body">
      <h2 class="intro__title">Natural Health &amp; Fitness</h2>
      <p class="intro__text">Our practice offers a wide scope of services, including health coaching and weight loss, all shaped around your goals and daily life.</p>
      <p class="intro__text">A patient services coordinator will help you choose the services that suit you best, from your first visit through every follow-up.</p>
      <p class="intro__text">We treat causes, not only symptoms, so you can feel stronger, move freely and enjoy lasting results.</p>
    </div>
  </article>

  <!-- Services -->
  <article class="panel services">
    <h2 class="services__title">Our Services</h2>
    <ul class="services__list">
      <li><svg width="14" height="14" viewBox="0 0 24 24"><path d="M4 12l5 5L20 6" fill="none" stroke="#abd036" stroke-width="3"/></svg>Primary Care</li>
      <li><svg width="14" height="14" viewBox="0 0 24 24"><path d="M4 12l5 5L20 6" fill="none" stroke="#abd036" stroke-width="3"/></svg>Health Coaching</li>
      <li><svg width="14" height="14" viewBox="0 0 24 24"><path d="M4 12l5 5L20 6" fill="none" stroke="#abd036" stroke-width="3"/></svg>Medical Weight Loss</li>
      <li><svg width="14" height="14" viewBox="0 0 24 24"><path d="M4 12l5 5L20 6" fill="none" stroke="#abd036" stroke-width="3"/></svg>Nutrition Counseling</li>
      <li><svg width="14" height="14" viewBox="0 0 24 24"><path d="M4 12l5 5L20 6" fill="none" stroke="#abd036" stroke-width="3"/></svg>Hormone Balance</li>
      <li><svg width="14" height="14" viewBox="0 0 24 24"><path d="M4 12l5 5L20 6" fill="none" stroke="#abd036" stroke-width="3"/></svg>Fitness Planning</li>
      <li><svg width="14" height="14" viewBox="0 0 24 24"><path d="M4 12l5 5L20 6" fill="none" stroke="#abd036" stroke-width="3"/></svg>Stress Management</li>
      <li><svg width="14" height="14" viewBox="0 0 24 24"><path d="M4 12l5 5L20 6" fill="none" stroke="#abd036" stroke-width="3"/></svg>Preventive Screenings</li>
      <li><svg width="14" height="14" viewBox="0 0 24 24"><path d="M4 12l5 5L20 6" fill="none" stroke="#abd036" stroke-width="3"/></svg>Chronic Care Support</li>
      <li><svg width="14" height="14" viewBox="0 0 24 24"><path d="M4 12l5 5L20 6" fill="none" stroke="#abd036" stroke-width="3"/></svg>Family Medicine</li>
    </ul>
    <p class="services__note">Ask our coordinator which programs fit your needs and insurance.</p>
    <div class="photo services__photo" role="img" aria-label="Photo of a woman stretching on an exercise mat"></div>
  </article>

  <!-- Doctors -->
  <article class="panel doctors">
    <div class="doctor doctor--one">
      <div class="doctor__photo" role="img" aria-label="Portrait photo of Dr. Elena Marsh"></div>
      <h3 class="doctor__name">Dr. Elena Marsh</h3>
      <p class="doctor__role">Medical Director</p>
      <p class="doctor__bio">Board-certified in family medicine with over fifteen years of practice, she blends modern treatment with lifestyle care to help patients thrive.</p>
    </div>
    <div class="doctor doctor--two">
      <div class="doctor__photo" role="img" aria-label="Portrait photo of Dr. Owen Brandt"></div>
      <h3 class="doctor__name">Dr. Owen Brandt</h3>
      <p class="doctor__role">Integrative Physician</p>
      <p class="doctor__bio">He focuses on nutrition, fitness and weight care, guiding each patient with clear plans and steady support toward better everyday health.</p>
    </div>
  </article>
</section>

</body>
</html>
```